Lark and Fern: Prespective and Balence in People's Lives Needs a Buissness Card Design

Lark and Fern Community Center is an organization that seeks to bring balance into people's lives. Main services include: guided meditation, group brainstorming, and guided counseling. Lark and Fern combines Eastern practices, i.e. Buddhism, Hinduism, and Taoism, with Western practices: therapy, group brainstorming and healing. We would like a double sided card: 1) front vertical with image, 2) back horizontal with information. The main colors for the card are red, white, black. Different finishes would be nice--please no high gloss. Matte, pearlized, embossing--used tactfully and sparingly would be nice. The card should convey balance/harmony in a modern world.

```html
<!DOCTYPE html>
<html lang="en">
<head>
<meta charset="utf-8">
<title>Lark and Fern Community Center — Business Card</title>
<link rel="stylesheet" href="https://fonts.googleapis.com/css2?family=Marcellus+SC&family=Open+Sans:wght@400;700&display=swap">
<style>
  :root {
    --stage: #2a2624;
    --ink: #141414;
    --paper: #ffffff;
    --red: #e0222a;
    --grey: #d8d8d8;
  }
  * { margin: 0; padding: 0; box-sizing: border-box; }
  html, body { width: 1200px; height: 716px; overflow: hidden; background: var(--stage); }
  .stage { position: relative; width: 1200px; height: 716px; }

  .card {
    position: absolute; top: 208px; width: 525px; height: 300px;
    overflow: hidden; background: var(--paper);
    box-shadow: 0 14px 30px rgba(0,0,0,.55);
  }

  /* Front */
  .card--front { left: 45px; }
  .front-top { position: absolute; inset: 0 0 50% 0; background: var(--ink); }
  .front-mark {
    position: absolute; left: 120px; top: 80px;
    display: flex; align-items: center; gap: 22px;
  }
  .front-mark .dot {
    width: 140px; height: 140px; border-radius: 50%;
    background: var(--red);
  }
  .front-mark .brand {
    font-family: "Marcellus SC", serif; font-size: 34px; color: var(--red);
    letter-spacing: 1px;
  }

  /* Back */
  .card--back { left: 630px; }
  .back-bottom { position: absolute; left: 0; right: 0; bottom: 0; height: 130px; }
  .back-bottom svg { position: absolute; inset: 0; width: 100%; height: 100%; }
  .identity { position: absolute; left: 150px; top: 48px; text-align: center; }
  .identity .brand {
    font-family: "Marcellus SC", serif; font-size: 42px; color: var(--red);
    line-height: 1; text-align: left; margin-left: -10px;
  }
  .identity .division {
    font-family: "Marcellus SC", serif; font-size: 15px; color: var(--ink);
    letter-spacing: 1px; text-align: left; margin-top: 4px;
  }
  .identity .person {
    font-family: "Marcellus SC", serif; font-size: 21px; color: var(--red);
    letter-spacing: 1px; margin-top: 14px;
  }
  .identity .role {
    font-family: "Marcellus SC", serif; font-size: 12px; color: var(--ink);
    letter-spacing: 1px;
  }
  .contact {
    position: absolute; left: 24px; bottom: 26px; list-style: none;
    font-family: "Open Sans", sans-serif; font-size: 13px; color: var(--paper);
    line-height: 1.6;
  }
  .contact .label { color: var(--red); display: inline-block; width: 30px; }
  .address {
    position: absolute; right: 24px; bottom: 22px; text-align: right;
    font-family: "Open Sans", sans-serif; font-size: 13px; color: var(--paper);
    line-height: 1.5;
  }
  .address .org { color: var(--red); font-weight: 700; }
</style>
</head>
<body>
<main class="stage">

  <section class="card card--front" aria-label="Card front">
    <div class="front-top"></div>
    <div class="front-mark">
      <span class="dot"></span>
      <span class="brand">Lark and Fern</span>
    </div>
  </section>

  <section class="card card--back" aria-label="Card back">
    <div class="identity">
      <div class="brand">Lark and Fern</div>
      <div class="division">Community Center</div>
      <div class="person">Marcus J. Hollowell</div>
      <div class="role">Director</div>
    </div>

    <div class="back-bottom">
      <svg viewBox="0 0 525 130" preserveAspectRatio="none" aria-hidden="true">
        <path d="M0 10 Q130 2 260 14 T525 40 L525 130 L0 130 Z" fill="#e0222a"/>
        <path d="M0 16 Q130 8 260 20 T525 46 L525 130 L0 130 Z" fill="#141414"/>
      </svg>
      <ul class="contact">
        <li><span class="label">[P]</span>555-014-2738</li>
        <li><span class="label">[E]</span>info@larkandfern.org</li>
        <li><span class="label">[W]</span>www.larkandfern.org</li>
      </ul>
      <address class="address" style="font-style:normal">
        <div class="org">Lark and Fern Community Center</div>
        <div>2280 Willowmere Ln</div>
        <div>Suite C4 Brookvale ST 00000</div>
      </address>
    </div>
  </section>

</main>
</body>
</html>
```